Create Lanternfield HR Business Cards.

Create Business Cards for Lanternfield HR. 2 sided and Would like the back to have the logo.

Info for Business Card:
Address: 4827 Millbrook Ave Suite 230 Cleveland, Ohio 44987
Office Number: 216-555-0143
Mobile: 216-555-0192

Website: www.lanternfieldhr.example

Target Market(s)

Small to medium size businesses

Industry/Entity Type

Human Resources

Contact Information for Business Card

Company logo and information

Font styles to use
Serif
Sans Serif

Requirements
Must have
• Info for Business Card: Address: 4827 Millbrook Ave Suite 230 Cleveland, Ohio 44987 Office Number: 216-555-0143 Mobile: 216-555-0192 Website: www.lanternfieldhr.example

```html
<!DOCTYPE html>
<html lang="en">
<head>
<meta charset="utf-8">
<title>Lanternfield HR Business Cards</title>
<link href="https://fonts.googleapis.com/css2?family=Arimo:wght@400;700&display=swap" rel="stylesheet">
<style>
  :root {
    --backdrop: #3a3a3a;
    --card-orange: #ff8500;
    --brand-orange: #f5861f;
    --brand-navy: #2b2468;
    --card-white: #ffffff;
    --text-grey: #555a63;
    --divider: #c9c9c9;
    --back-mark: #ffd21a;
  }
  * { box-sizing: border-box; margin: 0; padding: 0; }
  html, body {
    width: 1200px; height: 689px; overflow: hidden;
    background: var(--backdrop);
    font-family: "Arimo", Arial, sans-serif;
  }
  .canvas {
    position: relative; width: 1200px; height: 689px;
    display: flex; align-items: center; justify-content: center; gap: 50px;
  }
  .card {
    position: relative; width: 520px; height: 298px;
    border-radius: 18px; overflow: hidden;
  }
  /* Back side */
  .card-back {
    background: var(--card-orange);
    display: flex; align-items: center; justify-content: center; gap: 14px;
  }
  .card-back .brand-dot {
    width: 34px; height: 34px; border-radius: 50%; background: var(--back-mark);
  }
  .card-back .brand-name {
    font-weight: 700; font-size: 40px; color: var(--back-mark); letter-spacing: 0.5px;
  }
  /* Front side */
  .card-front { background: var(--card-white); }
  .front-brand {
    position: absolute; left: 34px; top: 92px; width: 190px;
    display: flex; align-items: center; gap: 10px;
  }
  .front-brand .brand-dot {
    flex: none; width: 22px; height: 22px; border-radius: 50%; background: var(--brand-orange);
  }
  .front-brand .brand-name {
    font-weight: 700; font-size: 26px; line-height: 1.1; color: var(--brand-navy);
  }
  .divider {
    position: absolute; left: 240px; top: 40px; width: 1px; height: 150px;
    background: linear-gradient(to bottom, transparent, var(--divider), transparent);
  }
  .contact { position: absolute; left: 264px; top: 42px; color: var(--text-grey); }
  .contact .person-name {
    font-weight: 700; font-size: 22px; color: var(--brand-navy); letter-spacing: 0.3px;
  }
  .contact .person-title { font-size: 13px; margin-top: 2px; }
  .contact .address { font-size: 13px; line-height: 1.35; margin-top: 14px; }
  .contact .phones { margin-top: 12px; font-size: 13px; line-height: 1.5; }
  .phone-line { display: flex; align-items: center; gap: 6px; }
  .phone-line svg { width: 11px; height: 11px; flex: none; }
  .footer-bands { position: absolute; left: 0; bottom: 0; width: 520px; height: 70px; }
  .website {
    position: absolute; right: 14px; bottom: 21px;
    font-size: 12.5px; color: var(--card-white); white-space: nowrap;
  }
</style>
</head>
<body>
<main class="canvas">
  <section class="card card-back" aria-label="Business card back">
    <span class="brand-dot"></span>
    <span class="brand-name">Lanternfield HR</span>
  </section>

  <section class="card card-front" aria-label="Business card front">
    <div class="front-brand">
      <span class="brand-dot"></span>
      <span class="brand-name">Lanternfield HR</span>
    </div>
    <div class="divider"></div>
    <div class="contact">
      <p class="person-name">JORDAN HALE</p>
      <p class="person-title">President</p>
      <p class="address">4827 Millbrook Ave<br>Suite 230<br>Cleveland, Ohio 44987</p>
      <div class="phones">
        <p class="phone-line">
          <svg viewBox="0 0 12 12"><path d="M2 1 L4.5 1 L5.3 3.6 L4 4.6 Q5 7 7.4 8 L8.4 6.7 L11 7.5 L11 10 Q5 11 1.5 5.5 Q1 3 2 1Z" fill="var(--brand-orange)"/></svg>
          216-555-0143
        </p>
        <p class="phone-line">
          <svg viewBox="0 0 12 12"><rect x="3" y="0.8" width="6" height="10.4" rx="1.2" fill="none" stroke="var(--brand-orange)" stroke-width="1.3"/></svg>
          216-555-0192
        </p>
      </div>
    </div>
    <svg class="footer-bands" viewBox="0 0 520 70" preserveAspectRatio="none">
      <polygon points="0,60 320,60 332,50 336,24 520,24 520,70 0,70" fill="var(--brand-navy)"/>
      <polygon points="0,50 318,50 328,42 328,47 320,55 0,55" fill="var(--brand-orange)"/>
    </svg>
    <p class="website">www.lanternfieldhr.example</p>
  </section>
</main>
</body>
</html>
```